Elementary School Profile of a Falconet

Please recreate a poster of our Profile of a Falconet traits that we desire to have when they graduate from 4th grade. This should be kid-friendly and kid-themed with icons to help communicate the Competencies. See attached six competencies and the "I can" statements next to. Our colors are navy, red and white. Our logo is attached as well. This will be made into a poster and displayed in each classroom, the office, and also used on social media.

```html
<!DOCTYPE html>
<html lang="en">
<head>
<meta charset="utf-8">
<title>Profile of a Falconet</title>
<link rel="stylesheet" href="https://fonts.googleapis.com/css2?family=Lilita+One&family=Poppins:wght@500;600&display=swap">
<style>
  :root {
    --backdrop: #adadad;
    --paper: #ffffff;
    --cream: #f8efe3;
    --card: #f8eee2;
    --red: #9b1c24;
    --navy: #0b4a7a;
    --gold: #f6b811;
    --ink: #3a3a3a;
    --c1: #3ea3cf;
    --c2: #0b4a7a;
    --c3: #9b1c24;
    --c4: #ee6c0f;
    --c5: #f8bb10;
    --c6: #b83590;
    --rule: #d2d2d2;
  }
  * { box-sizing: border-box; margin: 0; padding: 0; }
  html, body { width: 839px; height: 1200px; overflow: hidden; background: var(--backdrop); }
  .canvas { position: relative; width: 839px; height: 1200px; }
  .poster {
    position: absolute; left: 86px; top: 56px; width: 668px; height: 1088px;
    background: var(--paper); overflow: hidden;
    box-shadow: 0 2px 8px rgba(0,0,0,.25);
  }
  .poster-base { position: absolute; left: 0; bottom: 0; width: 100%; height: 13px; background: var(--navy); }
  .layer { position: absolute; left: 0; top: 0; width: 839px; height: 1200px; pointer-events: none; }

  .brand-mark {
    position: absolute; left: 112px; top: 96px; display: flex; align-items: center; gap: 6px;
    font-family: "Lilita One", sans-serif; font-size: 24px; color: var(--red);
  }
  .brand-mark .dot { width: 14px; height: 14px; border-radius: 50%; background: var(--red); }

  .title {
    position: absolute; left: 270px; top: 96px; width: 300px; text-align: center;
    font-family: "Lilita One", sans-serif; font-weight: 400; color: #fff; font-size: 33px; line-height: 37px;
    transform: rotate(2deg);
  }
  .badge-text {
    position: absolute; left: 586px; top: 100px; width: 130px; text-align: center;
    font-family: "Lilita One", sans-serif; color: #fff; font-size: 16px; line-height: 17px;
    transform: rotate(-14deg);
  }

  .divider { position: absolute; left: 140px; width: 561px; border-top: 1px dashed var(--rule); }

  .card {
    position: absolute; left: 137px; width: 323px; background: var(--card); border-radius: 9px;
    font-family: "Poppins", sans-serif; font-weight: 500; color: var(--ink); font-size: 9px; line-height: 12.5px;
  }
  .tab {
    position: absolute; height: 25px; width: 171px; border-radius: 13px; color: #fff;
    font-family: "Lilita One", sans-serif; font-size: 18px; line-height: 25px; text-align: center;
    background: var(--tab);
  }
  .tab::after {
    content: ""; position: absolute; left: 50%; bottom: -5px; margin-left: -6px;
    border-left: 6px solid transparent; border-right: 6px solid transparent; border-top: 6px solid var(--tab);
  }
  .traits { list-style: none; position: absolute; left: 42px; right: 8px; }
  .traits li { position: relative; }
  .traits li::before {
    content: ""; position: absolute; left: -22px; top: 2px; width: 8px; height: 8px; border-radius: 50%; background: var(--tick);
  }
  .traits li::after {
    content: ""; position: absolute; left: -20px; top: 3.6px; width: 2.5px; height: 4px;
    border: solid #fff; border-width: 0 1.2px 1.2px 0; transform: rotate(45deg);
  }
  .traits .one-line { white-space: nowrap; letter-spacing: -0.15px; }

  .icon-spot { position: absolute; left: 588px; width: 112px; border-radius: 40% 40% 50% 50% / 45% 45% 30% 30%; }

  .num {
    position: absolute; left: 487px; width: 74px; height: 74px; line-height: 74px; text-align: center;
    font-family: "Lilita One", sans-serif; font-size: 38px; color: #fff;
  }
</style>
</head>
<body>
<div class="canvas">
  <div class="poster">
    <div class="poster-base"></div>
  </div>

  <svg class="layer" viewBox="0 0 839 1200" aria-hidden="true">
    <defs>
      <linearGradient id="spine" x1="0" y1="0" x2="0" y2="1">
        <stop offset="0" stop-color="#3ea3cf"/>
        <stop offset=".18" stop-color="#0b4a7a"/>
        <stop offset=".4" stop-color="#9b1c24"/>
        <stop offset=".58" stop-color="#ee6c0f"/>
        <stop offset=".76" stop-color="#f8bb10"/>
        <stop offset="1" stop-color="#b83590"/>
      </linearGradient>
    </defs>
    <path d="M86 56 H754 V198 Q420 60 86 198 Z" fill="#f8efe3"/>
    <path d="M86 198 Q420 60 754 198" fill="none" stroke="#f6b811" stroke-width="7"/>
    <path d="M272 105 Q418 60 568 105 Q582 111 574 124 L532 180 Q526 189 514 188 Q418 170 326 188 Q314 189 308 180 L266 124 Q258 111 272 105 Z"
          fill="#9b1c24" stroke="#fff" stroke-width="5"/>
    <circle cx="651" cy="133" r="64" fill="#0b4a7a"/>
    <circle cx="651" cy="133" r="66" fill="none" stroke="#0b4a7a" stroke-width="10" stroke-dasharray="7 6" stroke-linecap="round"/>
    <rect x="519" y="254" width="10" height="792" fill="url(#spine)"/>
    <circle cx="524" cy="254" r="37" fill="#3ea3cf"/>
    <circle cx="524" cy="393" r="37" fill="#0b4a7a"/>
    <circle cx="524" cy="553" r="37" fill="#9b1c24"/>
    <circle cx="524" cy="711" r="37" fill="#ee6c0f"/>
    <circle cx="524" cy="873" r="37" fill="#f8bb10"/>
    <circle cx="524" cy="1045" r="37" fill="#b83590"/>
  </svg>

  <div class="brand-mark"><span class="dot"></span>Falconet</div>
  <h1 class="title">Profile Of<br>A Falconet</h1>
  <div class="badge-text">Early<br>Learners and<br>Elementary<br>School</div>

  <div class="divider" style="top:314px"></div>
  <div class="divider" style="top:469px"></div>
  <div class="divider" style="top:623px"></div>
  <div class="divider" style="top:793px"></div>
  <div class="divider" style="top:934px"></div>

  <!-- 01 -->
  <section class="card" style="top:208px;height:93px;--tick:var(--gold)">
    <ul class="traits" style="top:26px">
      <li style="margin-bottom:7px">Expresses ideas clearly and respectfully (written &amp; verbal).</li>
      <li style="margin-bottom:7px">Listens actively and understands diverse perspectives.</li>
      <li>Adjusts communication to suit the audience and context.</li>
    </ul>
  </section>
  <div class="tab" style="left:160px;top:195px;--tab:var(--c1)">Communicator</div>
  <div class="num" style="top:217px">01</div>
  <div class="icon-spot" role="img" aria-label="Megaphone on a grassy mound" style="top:190px;height:111px;background:linear-gradient(180deg,#6cc4ec 0%,#a8d45a 60%,#9bbf2a 100%)"></div>

  <!-- 02 -->
  <section class="card" style="top:341px;height:111px;--tick:var(--c2)">
    <ul class="traits" style="top:24px;left:42px">
      <li style="margin-bottom:7px">Questions, analyzes, and evaluates information<br>from multiple sources.</li>
      <li style="margin-bottom:7px">Identifies and solves complex problems creatively.</li>
      <li>Uses evidence and diverse perspectives to form<br>reasoned conclusions and make informed decisions.</li>
    </ul>
  </section>
  <div class="tab" style="left:154px;top:328px;--tab:var(--c2)">Critical Thinker</div>
  <div class="num" style="top:356px">02</div>
  <div class="icon-spot" role="img" aria-label="Glowing light bulb on a grassy mound" style="top:330px;height:125px;background:linear-gradient(180deg,#fbd232 0%,#f3c527 45%,#b4d43c 70%,#9bbf2a 100%)"></div>

  <!-- 03 -->
  <section class="card" style="top:504px;height:104px;--tick:var(--c3);font-size:8px;line-height:11.5px">
    <ul class="traits" style="top:24px;left:46px;right:4px">
      <li style="margin-bottom:7px">Takes ownership of actions, choices, and commitments<br>now and in future aspirations.</li>
      <li style="margin-bottom:7px">Takes pride in managing time, resources, and self while<br>striving to meet high expectations.</li>
      <li class="one-line">Acts with integrity while advocating for themselves and others.</li>
    </ul>
  </section>
  <div class="tab" style="left:160px;top:486px;--tab:var(--c3)">Responsible</div>
  <div class="num" style="top:516px">03</div>
  <div class="icon-spot" role="img" aria-label="Person with task, gear and check icons on a grassy mound" style="top:489px;height:119px;background:linear-gradient(180deg,#fde7a0 0%,#f8c21a 45%,#b4d43c 70%,#9bbf2a 100%)"></div>

  <!-- 04 -->
  <section class="card" style="top:650px;height:123px;--tick:var(--c4)">
    <ul class="traits" style="top:26px;left:42px">
      <li style="margin-bottom:8px">Responds productively to new situations, challenges,<br>and constructive feedback.</li>
      <li style="margin-bottom:8px">Learns from new experiences and applies prior<br>knowledge in an ever-changing world.</li>
      <li>Adjusts behavior and approach to engage effectively<br>with diverse groups and environments.</li>
    </ul>
  </section>
  <div class="tab" style="left:154px;top:638px;--tab:var(--c4)">Adaptable</div>
  <div class="num" style="top:674px">04</div>
  <div class="icon-spot" role="img" aria-label="Gear on a grassy mound" style="top:654px;height:119px;background:linear-gradient(180deg,#e4e6f3 0%,#7b92d0 45%,#b4d43c 72%,#9bbf2a 100%)"></div>

  <!-- 05 -->
  <section class="card" style="top:828px;height:86px;--tick:var(--c5)">
    <ul class="traits" style="top:26px;left:48px">
      <li style="margin-bottom:8px">Demonstrates strong teamwork by contributing<br>effectively and cooperatively toward shared goals.</li>
      <li>Listens actively and values diverse ideas<br>and perspectives.</li>
    </ul>
  </section>
  <div class="tab" style="left:160px;top:813px;--tab:var(--c5)">Collaborator</div>
  <div class="num" style="top:836px">05</div>
  <div class="icon-spot" role="img" aria-label="Colourful puzzle pieces on a grassy mound" style="top:802px;height:112px;background:linear-gradient(180deg,#6cc4ec 0%,#a3268a 30%,#f8bb10 55%,#b4d43c 75%,#9bbf2a 100%)"></div>

  <!-- 06 -->
  <section class="card" style="top:967px;height:140px;--tick:var(--c6)">
    <ul class="traits" style="top:24px;left:48px">
      <li style="margin-bottom:8px">Engages respectfully, knowing when to compromise,<br>support, or take the lead.</li>
      <li style="margin-bottom:8px">Understands and acknowledges others' feelings,<br>perspectives, and experiences.</li>
      <li style="margin-bottom:6px">Responds with kindness, patience, empathy, and support.</li>
      <li>Seeks to connect with others and contribute positively<br>to their well-being and the community's well-being.</li>
    </ul>
  </section>
  <div class="tab" style="left:160px;top:952px;--tab:var(--c6)">Compassionate</div>
  <div class="num" style="top:1008px">06</div>
  <div class="icon-spot" role="img" aria-label="Open hands holding a heart on a grassy mound" style="top:977px;height:130px;background:linear-gradient(180deg,#fbe1cc 0%,#ee7a5e 40%,#f7d6bf 60%,#b4d43c 78%,#9bbf2a 100%)"></div>
</div>
</body>
</html>
```